I want a flyer for a company that changes Incandescent bulbs and halogen bulbs in LED. The flyer can content this information and benefits that the LED can “give” you : With the help of LED's you will save up to 90% of the electricity bill, it helps the planet! They don't contain mercury, release carbon dioxide, they resist at lower temperatures, aren't sensitive to humidity, there haven't been any registered case of catching fire, release a bad odor or smoke from them, unlike incandescent and halogen bulbs. Their life spend is higher than 25000 hours! 5 years warranty

Do you want a better life? Do you want to help the planet? Do you want to save money? The LED light bulbs are the solution!
Discover the new and revolutionary way of illuminating your house with the help of LED light bulbs.

These are suggestions, you can do anything you can believe is better, I have no experience in advertising. My supplier is www.glowvane.co.uk , you can have a look there.

This leaflets will be distributed to the potential customers thru their post boxes.

I want to start the campaign ASAP, so waiting your ideas!!!

Industry/Entity Type

It Company

```html
<!DOCTYPE html>
<html lang="en">
<head>
<meta charset="utf-8">
<title>LED Bulb Flyers</title>
<link href="https://fonts.googleapis.com/css2?family=Open+Sans:wght@400;600;700&family=Oswald:wght@400;600&family=Special+Elite&display=swap" rel="stylesheet">
<style>
  :root {
    --backdrop: #2a2a2a;
    --sky: #41a6dc;
    --sky-deep: #1f78b8;
    --brand-blue: #1777c4;
    --headline-blue: #1368b6;
    --ink: #1b1b1b;
    --alert-red: #e0262b;
    --paper: #ffffff;
    --rule: #9a9a9a;
    --strip: #2b2b2b;
    --stamp-red: #c8242a;
  }
  * { margin: 0; padding: 0; box-sizing: border-box; }
  html, body { width: 1200px; height: 928px; overflow: hidden; background: var(--backdrop); }
  body { position: relative; font-family: "Open Sans", sans-serif; }
  .flyer { position: absolute; width: 528px; height: 748px; overflow: hidden; }
  .abs { position: absolute; }

  /* Front */
  .flyer-front { left: 61px; top: 71px;
    background: radial-gradient(ellipse at 50% 40%, var(--sky) 0%, #3b9ad3 60%, var(--sky-deep) 100%); }
  .front-frame { left: 28px; top: 30px; width: 471px; height: 688px; border: 1px solid rgba(255,255,255,.85); }
  .front-title { left: 0; width: 528px; text-align: center; color: var(--paper); white-space: nowrap; }
  .ruled { display: flex; align-items: center; justify-content: center; gap: 4px; }
  .ruled::before, .ruled::after { content: ""; width: 64px; height: 1px; background: var(--paper); }
  .line-discover { top: 76px; font-size: 15px; line-height: 18px; }
  .line-revolution { top: 94px; font-size: 15px; line-height: 18px; }
  .line-illuminate { top: 106px; font-size: 31px; line-height: 32px; font-weight: 400; }
  .line-help { top: 169px; font-size: 14px; line-height: 17px; }
  .ruled.line-help::before, .ruled.line-help::after { width: 38px; }
  .line-led { top: 184px; font-size: 25px; line-height: 30px; font-weight: 700; }
  .front-bulb { left: 150px; top: 267px; width: 232px; height: 175px; border-radius: 50%;
    background: radial-gradient(circle at 62% 40%, #fafafa 0%, #e6e6e6 40%, #b9c2c8 75%, rgba(65,166,220,0) 100%); }
  .front-company { top: 493px; font-size: 16px; line-height: 22px; font-weight: 700; letter-spacing: .3px; }
  .front-divider { left: 150px; top: 533px; width: 228px; height: 1px; background: rgba(255,255,255,.6); }
  .front-places { top: 546px; font-family: "Oswald", sans-serif; font-size: 16px; line-height: 22px; }
  .front-band { left: 28px; top: 552px; }
  .front-phone { top: 588px; font-size: 30px; line-height: 40px; font-weight: 700; color: var(--brand-blue); }
  .front-web { top: 630px; font-size: 13px; line-height: 18px; letter-spacing: 2px; color: var(--ink); }

  /* Back */
  .flyer-back { left: 622px; top: 101px; background: var(--paper); }
  .back-topbar { left: 0; top: 0; width: 528px; height: 19px; background: var(--brand-blue); }
  .back-portrait { left: 345px; top: 62px; width: 183px; height: 470px;
    background: linear-gradient(160deg, #6a3f2c 0%, #c99a80 35%, #f1ece8 70%, #ffffff 100%); }
  .back-questions { left: 39px; top: 46px; font-size: 15px; font-weight: 700; line-height: 20px; color: var(--ink); white-space: nowrap; }
  .back-headline { left: 38px; top: 108px; font-family: "Oswald", sans-serif; font-weight: 600;
    font-size: 36px; line-height: 35px; color: var(--headline-blue); white-space: nowrap;
    transform: scaleX(.8); transform-origin: left; }
  .back-rule { left: 40px; width: 260px; height: 1px; background: var(--rule); }
  .back-savings { left: 40px; top: 198px; color: var(--ink); white-space: nowrap; }
  .back-savings .lead { font-size: 15px; line-height: 20px; font-weight: 600; }
  .back-savings .big { font-family: "Oswald", sans-serif; font-size: 35px; line-height: 38px; color: var(--alert-red); }
  .back-savings .tail { font-size: 15px; line-height: 20px; font-weight: 600; }
  .benefit-list { left: 39px; top: 296px; list-style: none; font-size: 10.5px; line-height: 15px; color: var(--ink); white-space: nowrap; }
  .back-compare { left: 39px; top: 426px; font-size: 19px; font-weight: 700; line-height: 21px; color: var(--ink); }
  .back-life { left: 39px; top: 477px; font-size: 16px; line-height: 19px; color: var(--ink); }
  .back-base { left: 0; top: 520px; }
  .warranty-stamp { left: 180px; top: 524px; width: 170px; height: 64px; background: var(--paper);
    border: 3px solid var(--stamp-red); outline: 2px solid var(--paper); transform: rotate(-3deg);
    font-family: "Special Elite", monospace; color: var(--stamp-red); font-size: 24px; line-height: 26px;
    text-align: center; padding-top: 4px; box-shadow: 0 2px 6px rgba(0,0,0,.35); }
  .back-bulb { left: 15px; top: 585px; width: 142px; height: 105px; border-radius: 50%;
    background: radial-gradient(circle at 60% 42%, #fafafa 0%, #e4e4e4 40%, #b6bfc6 75%, rgba(23,119,196,0) 100%); }
  .back-company { left: 174px; top: 600px; font-size: 16px; line-height: 22px; font-weight: 700; color: var(--paper); letter-spacing: .3px; white-space: nowrap; }
  .back-phone { left: 194px; top: 625px; font-size: 40px; line-height: 54px; font-weight: 700; color: var(--paper); white-space: nowrap; }
  .back-strip { left: 0; top: 706px; width: 528px; height: 19px; background: var(--strip); }
  .back-bottombar { left: 0; top: 725px; width: 528px; height: 23px; background: var(--brand-blue); }
  .back-email { right: 124px; top: 708px; font-size: 10.5px; line-height: 15px; letter-spacing: 3px; color: var(--paper); white-space: nowrap; }
</style>
</head>
<body>

<section class="flyer flyer-front">
  <div class="abs front-frame"></div>
  <p class="abs front-title ruled line-discover">DISCOVER</p>
  <p class="abs front-title line-revolution">THE REVOLUTIONARY WAY OF</p>
  <h1 class="abs front-title line-illuminate">ILLUMINATING<br>YOUR HOUSE</h1>
  <p class="abs front-title ruled line-help">WITH THE HELP OF</p>
  <p class="abs front-title line-led">LED LIGHT BULBS</p>
  <div class="abs front-bulb" role="img" aria-label="Photo of a white LED light bulb"></div>
  <p class="abs front-title front-company">BRIGHTWELL HOME IMPROVEMENT LTD</p>
  <div class="abs front-divider"></div>
  <svg class="abs front-band" width="471" height="122" viewBox="0 0 471 122">
    <path d="M0 10 Q235 45 471 0 L471 116 Q235 90 0 112 Z" fill="#ffffff"/>
  </svg>
  <p class="abs front-title front-places">ASHCOMBE &nbsp;|&nbsp; MILLFORD &nbsp;|&nbsp; WESTSHIRE</p>
  <p class="abs front-title front-phone">07700 900 418</p>
  <p class="abs front-title front-web">www.brightwell-home.co.uk</p>
</section>

<section class="flyer flyer-back">
  <div class="abs back-topbar"></div>
  <div class="abs back-portrait" role="img" aria-label="Photo of a smiling woman in a white blouse pointing at the text"></div>
  <p class="abs back-questions">DO YOU WANT A BETTER LIFE?<br>DO YOU WANT TO HELP THE PLANET?<br>DO YOU WANT TO SAVE MONEY?</p>
  <h2 class="abs back-headline">THE LED LIGHT BULBS<br>ARE THE SOLUTION!</h2>
  <div class="abs back-rule" style="top:193px"></div>
  <div class="abs back-savings">
    <p class="lead">With the help of LED's you will</p>
    <p class="big">SAVE UP TO 90%</p>
    <p class="tail">of the electricity bill</p>
  </div>
  <div class="abs back-rule" style="top:282px"></div>
  <ul class="abs benefit-list">
    <li>It helps the planet!</li>
    <li>They don't contain mercury</li>
    <li>Release carbon dioxide</li>
    <li>They resist at lower temperatures</li>
    <li>Aren't sensitive to humidity</li>
    <li>There haven't been any registered case of catching fire</li>
    <li>Release a bad odor or smoke from them</li>
  </ul>
  <p class="abs back-compare">Unlike Incandescent<br>&amp; Halogen Bulbs</p>
  <p class="abs back-life">Their life spend is<br>higher than 25000 hours!</p>
  <svg class="abs back-base" width="528" height="186" viewBox="0 0 528 186">
    <path d="M0 20 Q264 -10 528 8 L528 186 L0 186 Z" fill="#b8b8b8"/>
    <path d="M0 26 Q264 -2 528 14 L528 186 L0 186 Z" fill="#1777c4"/>
  </svg>
  <div class="abs warranty-stamp">5 YEARS<br>WARRANTY</div>
  <div class="abs back-bulb" role="img" aria-label="Photo of a white LED light bulb"></div>
  <p class="abs back-company">BRIGHTWELL HOME IMPROVEMENT LTD</p>
  <p class="abs back-phone">07700 900 418</p>
  <div class="abs back-strip"></div>
  <div class="abs back-bottombar"></div>
  <p class="abs back-email">office@brightwell-home.co.uk</p>
</section>

</body>
</html>
```